1887 Basins & Spouts Business Card

I'm wanting to get a business card designed. Our business is 1887 Basins & Spouts
Details for the card:

1887 Basins & Spouts
Name: Warren Tobbit
Email: warren@1887basinsandspouts.com.au
Website: www.1887basinsandspouts.com.au
Mobile: 0438 169 204
Phone: 02 6187 4932

Font of Basins & Spouts is called Snell Roundhand. Not sue what font logo text is.

I'm thinking two sided but it doesn't have to be.

```html
<!DOCTYPE html>
<html lang="en">
<head>
<meta charset="utf-8">
<title>1887 Basins &amp; Spouts Business Card</title>
<link rel="stylesheet" href="https://fonts.googleapis.com/css2?family=Lato:wght@400;700&family=Montserrat:wght@700&display=swap">
<style>
  :root {
    --page: #3a3d42;
    --card-dark: #050505;
    --card-light: #ffffff;
    --ink: #111111;
    --ink-soft: #555555;
    --swoosh: #8a8a8a;
    --on-dark: #ffffff;
  }
  * { margin: 0; padding: 0; box-sizing: border-box; }
  html, body { width: 1200px; height: 1000px; overflow: hidden; }
  body {
    background: var(--page);
    font-family: "Lato", sans-serif;
    position: relative;
  }
  .card {
    position: absolute;
    left: 220px;
    width: 760px;
    height: 434px;
    border-radius: 20px;
    overflow: hidden;
  }
  .card--back { top: 40px; background: var(--card-dark); color: var(--on-dark); }
  .card--front { top: 520px; background: var(--card-light); color: var(--ink); }

  .brand { display: flex; align-items: center; gap: 18px; }
  .brand__mark { border-radius: 50%; flex: none; }
  .brand__name { font-weight: 400; line-height: 1.1; }
  .brand__tagline { font-size: 13px; letter-spacing: 0.2px; margin-top: 8px; }

  .card--back .brand { position: absolute; left: 170px; top: 120px; }
  .card--back .brand__mark { width: 92px; height: 92px; border: 3px solid var(--on-dark); }
  .card--back .brand__name { font-size: 36px; }
  .card--back .brand__tagline { font-size: 16px; }
  .back__footer {
    position: absolute; left: 0; right: 0; top: 320px;
    text-align: center; font-size: 20px;
  }

  .card--front .brand { position: absolute; left: 40px; top: 130px; gap: 12px; }
  .card--front .brand__mark { width: 64px; height: 64px; border: 2px solid var(--ink); }
  .card--front .brand__name { font-size: 24px; }
  .card--front .brand__tagline { font-size: 11px; color: var(--ink); }

  .divider {
    position: absolute; left: 398px; top: 120px;
    width: 1.5px; height: 170px; background: var(--ink);
  }
  .contact { position: absolute; left: 428px; top: 118px; }
  .contact__name {
    font-family: "Montserrat", sans-serif; font-weight: 700;
    font-size: 28px; color: var(--ink); margin-bottom: 12px;
  }
  .contact__list { list-style: none; }
  .contact__item {
    display: flex; align-items: center; gap: 12px;
    font-size: 17px; color: var(--ink-soft); line-height: 26px;
  }
  .contact__icon { width: 16px; height: 16px; flex: none; }
  .front__band { position: absolute; left: 0; bottom: 0; width: 760px; height: 434px; }
</style>
</head>
<body>

<section class="card card--back" aria-label="Card back">
  <div class="brand">
    <span class="brand__mark"></span>
    <div>
      <div class="brand__name">1887 Basins &amp; Spouts</div>
      <div class="brand__tagline">Combining timeless beauty with perfect practicality</div>
    </div>
  </div>
  <p class="back__footer">1887 Basins &amp; Spouts</p>
</section>

<section class="card card--front" aria-label="Card front">
  <svg class="front__band" viewBox="0 0 760 434" aria-hidden="true">
    <path d="M0,330 Q380,395 760,405 L760,434 L0,434 Z" fill="var(--card-dark)"/>
    <path d="M0,324 Q380,386 760,396" fill="none" stroke="var(--swoosh)" stroke-width="5"/>
  </svg>

  <div class="brand">
    <span class="brand__mark"></span>
    <div>
      <div class="brand__name">1887 Basins &amp; Spouts</div>
      <div class="brand__tagline">Combining timeless beauty with perfect practicality</div>
    </div>
  </div>

  <span class="divider"></span>

  <div class="contact">
    <h1 class="contact__name">Warren Tobbit</h1>
    <ul class="contact__list">
      <li class="contact__item">
        <svg class="contact__icon" viewBox="0 0 24 24"><path d="M6.6 10.8a15 15 0 0 0 6.6 6.6l2.2-2.2a1 1 0 0 1 1-.25 11.4 11.4 0 0 0 3.6.57 1 1 0 0 1 1 1V20a1 1 0 0 1-1 1A17 17 0 0 1 3 4a1 1 0 0 1 1-1h3.5a1 1 0 0 1 1 1c0 1.25.2 2.45.57 3.57a1 1 0 0 1-.25 1z" fill="var(--ink)"/></svg>
        02 6187 4932
      </li>
      <li class="contact__item">
        <svg class="contact__icon" viewBox="0 0 24 24"><rect x="6" y="2" width="12" height="20" rx="2" fill="none" stroke="var(--ink)" stroke-width="2"/><circle cx="12" cy="18" r="1.2" fill="var(--ink)"/></svg>
        0438 169 204
      </li>
      <li class="contact__item">
        <svg class="contact__icon" viewBox="0 0 24 24"><rect x="2" y="5" width="20" height="14" rx="1" fill="var(--ink)"/><path d="M3 6l9 7 9-7" fill="none" stroke="#fff" stroke-width="1.8"/></svg>
        warren@1887basinsandspouts.com.au
      </li>
      <li class="contact__item">
        <svg class="contact__icon" viewBox="0 0 24 24"><circle cx="12" cy="12" r="10" fill="var(--ink)"/><path d="M2 12h20M12 2c3 3 3 17 0 20M12 2c-3 3-3 17 0 20" fill="none" stroke="#fff" stroke-width="1.4"/></svg>
        www.1887basinsandspouts.com.au
      </li>
    </ul>
  </div>
</section>

</body>
</html>
```